Fahrzeugbeschriftung für Potovoltaik-Solaranlagen
Zielgruppe
PV-Solaranlagen für Privat, Gewerbe und Industrie
Aufgabenstellung
existierendes Logo und einen 'flotten Spruch', etwa:'....Solaranlagen vom Profi“ Brandauer Strom-Technik GmbH, Meisterbetrieb Beschriftung soll nur am Heck von Falko Reisebus R4.2 angebracht werden
Das Fzg. Hat rundum Scheiben und ist Schwarz.

```html
<!DOCTYPE html>
<html lang="de">
<head>
<meta charset="utf-8">
<title>Heckscheibe – Brandauer Strom-Technik</title>
<link rel="stylesheet" href="https://fonts.googleapis.com/css2?family=Montserrat:wght@400;500&display=swap">
<style>
  :root {
    --page: #eef0f2;
    --sky-light: #27d6e6;
    --sky-mid: #1a9fd0;
    --panel-deep: #0d3a78;
    --panel-mid: #1556a6;
    --grass: #1f7a45;
    --grass-deep: #0f4a3a;
    --leaf: #8cc63f;
    --text: #f4f5f4;
  }
  * { margin: 0; padding: 0; box-sizing: border-box; }
  html, body {
    width: 1200px;
    height: 1176px;
    overflow: hidden;
    background: var(--page);
  }
  .rear-window {
    position: absolute;
    left: 40px;
    top: 381px;
    width: 1120px;
    height: 413px;
    border-radius: 60px 60px 22px 22px / 40px 40px 22px 22px;
    overflow: hidden;
    font-family: "Montserrat", sans-serif;
    color: var(--text);
  }
  .scene-backdrop {
    position: absolute;
    inset: 0;
    background:
      radial-gradient(ellipse 18% 30% at 88% 8%, rgba(255,255,255,0.95), rgba(255,255,255,0) 70%),
      linear-gradient(160deg, rgba(13,58,120,0) 45%, rgba(31,122,69,0.9) 75%, var(--grass-deep) 100%),
      linear-gradient(180deg, var(--sky-light) 0%, var(--sky-mid) 18%, var(--panel-mid) 40%, var(--panel-deep) 80%, #0b2f5e 100%);
  }
  .brand-mark {
    position: absolute;
    left: 110px;
    top: 100px;
    width: 190px;
    height: 190px;
    border-radius: 50%;
    background: var(--leaf);
  }
  .brand-name {
    position: absolute;
    left: 366px;
    top: 98px;
    font-size: 104px;
    font-weight: 500;
    line-height: 1;
    letter-spacing: -2px;
    color: var(--text);
  }
  .tagline {
    position: absolute;
    left: 372px;
    top: 232px;
    font-size: 50px;
    font-weight: 400;
    letter-spacing: 2px;
    line-height: 1;
    text-shadow: 1px 2px 3px rgba(0,0,0,0.45);
  }
  .contact {
    position: absolute;
    top: 350px;
    font-size: 34px;
    font-weight: 500;
    line-height: 1;
    text-shadow: 1px 2px 3px rgba(0,0,0,0.45);
  }
  .contact--phone { left: 58px; }
  .contact--mail { right: 56px; }
</style>
</head>
<body>
  <section class="rear-window">
    <div class="scene-backdrop" role="img" aria-label="Foto: Reihen von Solarmodulen auf grüner Wiese unter blauem Himmel mit Sonne und Bäumen"></div>
    <div class="brand-mark"></div>
    <div class="brand-name">BRANDAUER</div>
    <div class="tagline">Strom-Technik</div>
    <div class="contact contact--phone">0 47 11 - 385 60 27</div>
    <div class="contact contact--mail">stromtechnik@mailhafen</div>
  </section>
</body>
</html>
```